Business Card Design

An energy company designed around renewable energy and energy storage that focuses on providing its energy at points on the grid that reduce costs and add value to the system.

Industry/Entity Type

Business

Contact Information for Business Card

Martin Delacroix
Executive Vice President
41 K ST NE
Washington, DC 20017
240-555-0183
mdelacroix@harborvoltco.example

```html
<!DOCTYPE html>
<html lang="en">
<head>
<meta charset="utf-8">
<title>Business Card – Martin Delacroix</title>
<link href="https://fonts.googleapis.com/css2?family=Oswald:wght@400;500;700&display=swap" rel="stylesheet">
<style>
  :root {
    --page-bg: #f1eff0;
    --card-edge: #ffffff;
    --card-face: #000000;
    --ink-light: #ffffff;
    --ink-muted: #8c8c8c;
    --ink-contact: #c9c9c9;
  }
  html, body {
    margin: 0;
    width: 1200px;
    height: 845px;
    overflow: hidden;
    background: var(--page-bg);
  }
  .stage {
    width: 1200px;
    height: 845px;
    display: flex;
    align-items: center;
    justify-content: center;
  }
  .business-card {
    width: 840px;
    height: 480px;
    box-sizing: border-box;
    background: var(--card-edge);
    padding: 14px;
    box-shadow: 0 10px 30px rgba(0,0,0,0.12);
  }
  .card-face {
    width: 100%;
    height: 100%;
    background: var(--card-face);
    display: flex;
    align-items: center;
    justify-content: center;
    gap: 18px;
    padding-top: 40px;
    box-sizing: border-box;
  }
  .identity {
    font-family: "Oswald", sans-serif;
    text-transform: uppercase;
    line-height: 0.95;
  }
  .identity-name {
    margin: 0;
    font-weight: 700;
    font-size: 42px;
    letter-spacing: 1px;
    color: var(--ink-light);
  }
  .identity-title {
    margin: 2px 0 0;
    font-weight: 500;
    font-size: 33px;
    letter-spacing: 1.5px;
    color: var(--ink-muted);
  }
  .contact-list {
    list-style: none;
    margin: 0 0 34px;
    padding: 0;
    font-family: "Oswald", sans-serif;
    text-transform: uppercase;
    font-size: 15px;
    letter-spacing: 1px;
    color: var(--ink-contact);
  }
  .contact-item {
    display: flex;
    align-items: center;
    gap: 8px;
    line-height: 22px;
  }
  .contact-icon {
    width: 16px;
    height: 16px;
    fill: var(--ink-light);
    flex: none;
  }
</style>
</head>
<body>
  <main class="stage">
    <article class="business-card">
      <div class="card-face">
        <header class="identity">
          <h1 class="identity-name">Martin Delacroix</h1>
          <p class="identity-title">Executive Vice President</p>
        </header>
        <ul class="contact-list">
          <li class="contact-item">
            <svg class="contact-icon" viewBox="0 0 16 16" aria-hidden="true">
              <path d="M8 1a4.5 4.5 0 0 0-4.5 4.5C3.5 9 8 15 8 15s4.5-6 4.5-9.5A4.5 4.5 0 0 0 8 1zm0 6.3a1.8 1.8 0 1 1 0-3.6 1.8 1.8 0 0 1 0 3.6z"/>
            </svg>
            <span>41 K St NE Washington, DC 20017</span>
          </li>
          <li class="contact-item">
            <svg class="contact-icon" viewBox="0 0 16 16" aria-hidden="true">
              <path d="M1 5.5C1 4 4 2.5 8 2.5s7 1.5 7 3v1.3l-3 .7-.8-1.8C10.3 5.4 9.2 5.3 8 5.3s-2.3.1-3.2.4L4 7.5l-3-.7zM4 8.5l1.5-2h5l1.5 2v5H4zm4 1a1.6 1.6 0 1 0 0 3.2A1.6 1.6 0 0 0 8 9.5z"/>
            </svg>
            <span>240-555-0183</span>
          </li>
          <li class="contact-item">
            <svg class="contact-icon" viewBox="0 0 16 16" aria-hidden="true">
              <path d="M1 3.5h14v9H1zm1.4 1.2v.3L8 9l5.6-4v-.3zm0 1.8v4.8h11.2V6.5L8 10.6z"/>
            </svg>
            <span>mdelacroix@harborvoltco.example</span>
          </li>
        </ul>
      </div>
    </article>
  </main>
</body>
</html>
```